Velisto Events Business Card

We need a business cards that stands out to our clients. We are company who targets prestige clients to spend money with us on experiences, so our image needs to be prestige
Target Market(s)
Corporate
Contact Information for Business Card
There will be four different names on the business cards
Dana Morrowby
Director
O: 02 5147 3086
M: 0451 692 038
E: info@velistoevents.example.au
Facebook: @velistoevents
Instagram: velistoevents
www.velistoevents.example.au
Nathaniel Morrowby
Director
O: 02 5147 3086
M: 0467 215 904
Facebook: @velistoevents
Instagram: velistoevents
www.velistoevents.example.au
Teodor Vinkel
Director
O: 02 5147 3086
M: 0478 903 527
Facebook: @velistoevents
Instagram: velistoevents
www.velistoevents.example.au
Mabel Hartung
Director
O: 02 5147 3086
Facebook: @velistoevents
Instagram: velistoevents
www.velistoevents.example.au
Colors
Designer to choose colors to be used in the design.
Look and feel

```html
<!DOCTYPE html>
<html lang="en">
<head>
<meta charset="utf-8">
<title>Velisto Events Business Card</title>
<link rel="stylesheet" href="https://fonts.googleapis.com/css2?family=Archivo:wght@400;800&display=swap">
<style>
  :root {
    --navy: #25224f;
    --gold: #c9a45a;
    --ink: #25224f;
    --paper: #ffffff;
    --backdrop: #f4f4f6;
  }
  * { margin: 0; padding: 0; box-sizing: border-box; }
  html, body { width: 959px; height: 1200px; overflow: hidden; background: var(--backdrop); }
  body { position: relative; font-family: "Archivo", Arial, sans-serif; color: var(--ink); }

  .card { position: absolute; left: 60px; width: 838px; height: 479px; background: var(--paper); }
  .card--front { top: 81px; }
  .card--back { top: 638px; }

  .brand-panel { position: absolute; left: 255px; width: 328px; background: var(--navy);
    display: flex; flex-direction: column; align-items: center; justify-content: center; }
  .card--front .brand-panel { top: 0; height: 209px; padding-top: 90px; }
  .card--back .brand-panel { top: 0; height: 479px; padding-top: 150px; }

  .wordmark { color: var(--gold); font-weight: 400; text-align: center; line-height: 1; }
  .wordmark__name { display: block; letter-spacing: 0.32em; margin-right: -0.32em; }
  .wordmark__sub { display: block; letter-spacing: 0.38em; margin-right: -0.38em; }
  .card--front .wordmark__name { font-size: 23px; }
  .card--front .wordmark__sub { font-size: 11px; margin-top: 8px; }
  .card--back .wordmark__name { font-size: 34px; }
  .card--back .wordmark__sub { font-size: 18px; margin-top: 14px; }

  .holder { position: absolute; top: 220px; left: 0; width: 100%; text-align: center; }
  .holder__name { font-weight: 800; font-size: 37px; line-height: 1; letter-spacing: 0.01em; }
  .holder__role { font-size: 16px; margin-top: 2px; }

  .divider { position: absolute; top: 315px; left: 117px; width: 604px; height: 2px; background: var(--navy); }

  .contact { position: absolute; display: flex; align-items: center; gap: 18px; font-size: 15.5px; white-space: nowrap; }
  .contact__icon { width: 19px; height: 19px; flex: none; }
  .contact--address { top: 364px; left: 280px; }
  .contact--office { top: 402px; left: 116px; }
  .contact--mobile { top: 402px; left: 293px; }
  .contact--email { top: 402px; left: 470px; }
</style>
</head>
<body>
  <section class="card card--front">
    <div class="brand-panel">
      <div class="wordmark">
        <span class="wordmark__name">VELISTO</span>
        <span class="wordmark__sub">EVENTS</span>
      </div>
    </div>
    <div class="holder">
      <h1 class="holder__name">YOUR NAME</h1>
      <p class="holder__role">FOUNDER</p>
    </div>
    <div class="divider"></div>

    <p class="contact contact--address">
      <svg class="contact__icon" viewBox="0 0 20 20"><rect width="20" height="20" fill="#25224f"/><path d="M4 10 L10 4.5 L16 10 L14.5 10 L14.5 16 L11.5 16 L11.5 12 L8.5 12 L8.5 16 L5.5 16 L5.5 10 Z" fill="#fff"/></svg>
      YOUR ADDRESS COMES HERE
    </p>
    <p class="contact contact--office">
      <svg class="contact__icon" viewBox="0 0 20 20"><rect width="20" height="20" fill="#25224f"/><path d="M6 4.5 L8.3 4.5 L9 7.8 L7.6 9 Q9 11.8 11.2 12.6 L12.3 11.2 L15.5 12 L15.5 14.3 Q15 15.5 13.5 15.5 Q6 14.5 4.5 6.5 Q4.6 5 6 4.5 Z" fill="#fff"/></svg>
      +000 000 000
    </p>
    <p class="contact contact--mobile">
      <svg class="contact__icon" viewBox="0 0 20 20"><rect width="20" height="20" fill="#25224f"/><rect x="6.5" y="3.5" width="7" height="13" rx="1" fill="none" stroke="#fff" stroke-width="1.4"/><circle cx="10" cy="14.3" r="0.8" fill="#fff"/></svg>
      +000 000 000
    </p>
    <p class="contact contact--email">
      <svg class="contact__icon" viewBox="0 0 20 20"><rect width="20" height="20" fill="#25224f"/><rect x="4" y="6" width="12" height="8.5" fill="none" stroke="#fff" stroke-width="1.3"/><path d="M4 6 L10 11 L16 6 M4 14.5 L8.5 10 M16 14.5 L11.5 10" fill="none" stroke="#fff" stroke-width="1.2"/></svg>
      info@velistoevents.example.au
    </p>
  </section>

  <section class="card card--back">
    <div class="brand-panel">
      <div class="wordmark">
        <span class="wordmark__name">VELISTO</span>
        <span class="wordmark__sub">EVENTS</span>
      </div>
    </div>
  </section>
</body>
</html>
```